Mens Jewellery Homepage - Modern, Stylish Mens Ring Brand - Homepage

Project Overview: TorvikLoops.com is a men's accessories brand specializing in high-quality mens rings.

The objective of this redesign is to create a modern, visually appealing homepage that is easy to navigate, showcases a wide range of rings, highlights personalization options, and builds trust with customers.

The new design should make a strong impression while reflecting the brand's premium quality and commitment to craftsmanship.

The focus will be on a sleek aesthetic that aligns with the tastes of men shopping for wedding bands, engagement rings, or fashion accessories.

Objectives:

Modern and Sleek Aesthetic:

A clean, minimalist design that emphasizes high-quality product imagery and thoughtful use of space.
Contemporary color palette that conveys elegance and sophistication, with accents that highlight key elements without overwhelming the user.

Consistent and easy-to-read typography that reflects the brand’s modern and masculine identity.

Showcasing Products:
Hero Section: A image to show off 3 or 4 ring designs that could be used for weddings or fashion.

Product Highlights: Below the hero banner, showcase product categories by color (see current website for colors)

Featured Products: Display a selection of “Top Rated” or “Customer Favorites” rings to help guide users toward popular choices.

Personalization Section:
A dedicated section promoting the ability to personalize rings, emphasizing features like engraving with names, dates, or special messages.
Include lifestyle images of personalized rings to inspire customers and give them an idea of what’s possible.
Use callouts such as “Make It Yours” or “Personalize Your Ring” to encourage users to explore the customization options available for each product.

Building Trust:

A space to show 5 or 6 testimonials and other trust elements

Symbols / text to show

free delivery
free returns
every ring stock
fast delivery
customer images (from reviews)

Driving Conversions:
Include a prominent call-to-action (CTA) button in the hero section with text like “Shop Now” or “Discover Our Collections.”

User Experience:
Fast, easy-to-navigate layout with simple and intuitive categories. Product categories and main sections should be clearly visible and easy to access without overwhelming the user.
Design the homepage to feel cohesive and uncluttered, with a logical flow from product discovery to personalization and checkout.

Visual Elements and Imagery:
Use ring images from our site, but add backgrounds etc to make the image on the homepage more interesting.

Personalization Options: Use visual representations (like ring mockups) showing where personalization options (such as engravings) would appear on the product.

I like (and would like to see some different designs from our current design)
Brix.com for design
stoutcircles.com

Target Market(s)

Men - 20 to 35

Number of Pages Required

1 page

Requirements
Must have
• Easy navigation, Trust, Modern, Clean,
Nice to have
• Would like to see Different designs like Brix.com - StoutCircles.com

```html
<!DOCTYPE html>
<html lang="en">
<head>
<meta charset="utf-8">
<title>Torvik Loops – Handcrafted Men's Rings</title>
<link rel="stylesheet" href="https://fonts.googleapis.com/css2?family=Great+Vibes&family=Montserrat:wght@400;500;600;700&display=swap">
<style>
:root{
  --wine:#8e0f14;
  --wine-deep:#6a0a0e;
  --wine-light:#b51c22;
  --footer:#7a0e12;
  --gold:#f6dc8e;
  --gold-text:#3a2a08;
  --cream:#fdf1e6;
  --peach:#fbe0c4;
  --ink:#2b2b2b;
  --muted:#5c5c5c;
  --teal:#0f6b73;
  --white:#ffffff;
  --grey-bg:#f7f7f7;
  --script:"Great Vibes", cursive;
  --sans:"Montserrat", sans-serif;
}
*{box-sizing:border-box;margin:0;padding:0}
html,body{width:1200px;height:4120px;overflow:hidden}
body{position:relative;font-family:var(--sans);color:var(--ink);background:var(--white)}
.abs{position:absolute}
a{color:inherit;text-decoration:none}
.script-title{font-family:var(--script);font-weight:400;color:var(--ink);text-align:center;position:absolute;left:0;width:1200px;font-size:46px;line-height:1.1}

/* hero */
.hero{position:absolute;left:0;top:0;width:1200px;height:541px;background:radial-gradient(ellipse at 68% 40%,var(--wine-light) 0%,var(--wine) 45%,var(--wine-deep) 100%);color:var(--white)}
.brand{position:absolute;display:flex;align-items:center;gap:10px;color:var(--white);font-family:var(--sans);font-weight:600;font-size:15px;letter-spacing:4px;white-space:nowrap}
.brand-dot{width:44px;height:44px;border:2.5px solid var(--white);border-radius:50%}
.nav{position:absolute;top:40px;left:510px;display:flex;gap:30px;font-size:14px;font-weight:600;letter-spacing:.3px}
.hero-kicker{position:absolute;left:112px;top:158px;font-family:var(--script);font-size:32px}
.hero-title{position:absolute;left:118px;top:202px;font-family:var(--script);font-size:80px;line-height:1}
.hero-sub{position:absolute;left:202px;top:290px;font-family:var(--script);font-size:30px}
.btn-gold{position:absolute;background:var(--gold);color:var(--gold-text);font-weight:600;font-size:15px;border-radius:6px;display:flex;align-items:center;justify-content:center}
.hero-dots{position:absolute;left:112px;top:495px;display:flex;gap:6px}
.hero-dots span{height:4px;width:14px;background:rgba(255,255,255,.6);border-radius:2px}
.hero-dots span:first-child{width:40px;background:var(--white)}

/* categories */
.cat{position:absolute;top:687px;width:170px;text-align:center;font-size:15.5px;font-weight:500;line-height:25px;color:var(--ink)}
.cat .disc{width:120px;height:120px;border-radius:50%;margin:0 auto 14px;border:2px solid #f2dcc4}

/* products */
.card{position:absolute;top:1040px;width:213px;height:253px;background:var(--white);border-radius:8px;box-shadow:0 2px 14px rgba(0,0,0,.08);text-align:center}
.card.active{background:#efe2d2}
.card .pic{width:90px;height:70px;margin:24px auto 0;border-radius:40px}
.card .name{font-size:15px;font-weight:500;line-height:25px;margin-top:20px;padding:0 14px}
.card .price{color:var(--teal);font-weight:700;font-size:18px;margin-top:16px}
.card .icons{position:absolute;right:22px;top:20px;display:flex;flex-direction:column;gap:10px}
.pager{position:absolute;top:1339px;left:564px;display:flex;gap:5px}
.pager span{width:9px;height:9px;border-radius:50%;background:#bfe0e2}
.pager span:first-child{background:var(--teal)}

/* styles */
.styles{position:absolute;left:0;top:1437px;width:1200px;height:582px;background:var(--cream)}
.style-item{position:absolute;left:627px;width:500px;font-size:12.5px;color:var(--muted);line-height:27px;white-space:nowrap}
.style-item h3{font-size:16px;font-weight:600;color:var(--ink);line-height:22px;margin-bottom:4px}
.style-item em{font-style:normal;color:var(--wine-light)}

/* personalise */
.personal{position:absolute;left:0;top:2019px;width:1200px;height:640px;background:linear-gradient(var(--grey-bg),var(--white))}
.personal-copy{position:absolute;left:112px;top:2158px;width:550px;font-size:12.5px;line-height:26px;color:#444}
.personal-copy em{font-style:normal;color:var(--wine-light)}
.btn-dark{position:absolute;left:112px;top:2555px;width:221px;height:44px;background:#333;color:var(--white);font-weight:600;font-size:15px;border-radius:5px;display:flex;align-items:center;justify-content:center;box-shadow:0 3px 8px rgba(0,0,0,.25)}

/* reviews */
.review{position:absolute;width:355px;background:var(--white);border-radius:6px;box-shadow:0 2px 16px rgba(0,0,0,.09);padding:22px 22px;font-size:14.5px;line-height:27px;color:var(--muted)}
.review h4{font-size:15px;font-weight:600;color:var(--ink);line-height:20px}
.stars{color:#f0b400;font-size:9px;letter-spacing:1px;line-height:14px;margin-bottom:8px}

/* wedding */
.wedding{position:absolute;left:0;top:3090px;width:1200px;height:456px;background:#1e1e1e}
.wedding-photo{position:absolute;left:706px;top:0;width:494px;height:456px;background:radial-gradient(ellipse at 45% 60%,#5a4630 0%,#2a2016 45%,#0f0c09 100%)}
.deco-rings{position:absolute;left:0;top:0;width:140px;height:130px;background:radial-gradient(ellipse at 30% 40%,#c9a45c 0%,#8d8d8d 40%,transparent 72%);opacity:.8}
.wedding-title{position:absolute;left:0;width:770px;top:3168px;text-align:center;font-family:var(--script);font-weight:400;font-size:46px;line-height:1.1;color:var(--white)}
.wedding-sub{position:absolute;left:0;width:770px;top:3232px;text-align:center;color:var(--white);font-size:16.5px;letter-spacing:.3px}

/* trust */
.trust-base{position:absolute;left:0;top:3546px;width:1200px;height:574px;background:var(--footer)}
.trust{position:absolute;left:141px;top:3424px;width:918px;height:219px;background:var(--peach);border-radius:12px}
.perk{position:absolute;display:flex;align-items:center;gap:14px;font-size:19px;font-weight:600;letter-spacing:1px;color:var(--ink);white-space:nowrap}
.perk svg{flex:none}

/* footer */
.foot-brand{font-size:12px;letter-spacing:2.5px;gap:8px}
.foot-col{position:absolute;top:3702px;color:var(--white)}
.foot-col h5{font-size:19px;font-weight:500;margin-bottom:18px}
.foot-col li{list-style:none;font-size:13px;line-height:20px;margin-bottom:12px;opacity:.92}
.rule{position:absolute;left:0;width:1200px;height:1px;background:rgba(255,255,255,.25)}
.contact{position:absolute;top:3994px;display:flex;align-items:center;gap:12px;color:var(--white);font-weight:600;font-size:16px}
.copy{position:absolute;left:112px;top:4075px;color:var(--white);font-size:12.5px}
.pay{position:absolute;top:4074px;left:762px;display:flex;gap:17px}
.pay span{width:34px;height:18px;border-radius:3px;background:rgba(255,255,255,.85)}
</style>
</head>
<body>

<!-- HERO -->
<header class="hero">
  <div class="brand" style="left:112px;top:28px"><span class="brand-dot"></span>TORVIK LOOPS</div>
  <nav class="nav">
    <a href="#">SHOP BY MATERIAL</a>
    <a href="#">SHOP BY COLOR</a>
    <a href="#">TRY AT HOME</a>
  </nav>
  <svg class="abs" style="left:1002px;top:38px" width="26" height="26" viewBox="0 0 26 26" fill="none" stroke="#fff" stroke-width="2.4"><circle cx="11" cy="11" r="8"/><path d="M17 17l7 7"/></svg>
  <svg class="abs" style="left:1062px;top:38px" width="26" height="26" viewBox="0 0 26 26" fill="#fff"><path d="M4 8h16l-1.5 14H5.5z"/><path d="M8 8V6a4 4 0 018 0v2" fill="none" stroke="#fff" stroke-width="2"/><circle cx="21" cy="20" r="4" fill="#fff" stroke="#8e0f14" stroke-width="1.5"/></svg>

  <div class="hero-kicker">Elevate Your Style:</div>
  <div class="hero-title">Handcrafted Rings</div>
  <div class="hero-sub">with Free Fast Delivery &amp; Hassle Free Returns</div>
  <a class="btn-gold" href="#" style="left:112px;top:356px;width:244px;height:45px">Discover Our Collections</a>

  <div class="abs" role="img" aria-label="Open gold ring box holding two wedding bands, with loose gold and silver rings beside it" style="left:720px;top:120px;width:350px;height:350px;background:radial-gradient(ellipse at 50% 55%,#e8c48a 0%,#b98c55 30%,rgba(142,15,20,0) 68%)"></div>

  <div class="hero-dots"><span></span><span></span><span></span><span></span></div>
</header>

<!-- CATEGORIES -->
<h2 class="script-title" style="top:608px">Our Product Categories</h2>
<div class="cat" style="left:93px"><div class="disc" role="img" aria-label="Black ring collection" style="background:radial-gradient(circle,#3a3a3a,#050505)"></div>Strong Fearless<br>Majestics</div>
<div class="cat" style="left:270px"><div class="disc" role="img" aria-label="Silver ring collection" style="background:radial-gradient(circle,#f5f5f5,#a7a7a7)"></div>Calm Sophisticated<br>Elegant</div>
<div class="cat" style="left:446px"><div class="disc" role="img" aria-label="Blue ring collection" style="background:radial-gradient(circle,#2aa4d8,#0a5a8a)"></div>Constant Loyal<br>True</div>
<div class="cat" style="left:601px"><div class="disc" role="img" aria-label="Gold ring collection" style="background:radial-gradient(circle,#fff2c0,#d9b559)"></div>Bright Brilliant<br>Classic</div>
<div class="cat" style="left:763px"><div class="disc" role="img" aria-label="Brown ring collection" style="background:radial-gradient(circle,#a8634a,#5a2a1c)"></div>Authentic<br>Genuine Simple</div>
<div class="cat" style="left:933px"><div class="disc" role="img" aria-label="Rose gold ring collection" style="background:radial-gradient(circle,#fde2cc,#f0b592)"></div>Romantic<br>Vintage Sublime</div>

<!-- TOP RATED -->
<h2 class="script-title" style="top:958px">Top Rated Products</h2>

<div class="card" style="left:112px">
  <div class="icons"><svg width="14" height="13" viewBox="0 0 14 13" fill="#c88a10"><path d="M0 1h3l2 8h7l2-6H4" fill="none" stroke="#c88a10" stroke-width="1.6"/><circle cx="6" cy="11.5" r="1.3"/><circle cx="11" cy="11.5" r="1.3"/></svg><svg width="14" height="13" viewBox="0 0 14 13"><path d="M7 12L1.5 6.5a3 3 0 015-4L7 3l.5-.5a3 3 0 015 4z" fill="none" stroke="#c88a10" stroke-width="1.3"/></svg></div>
  <div class="pic" role="img" aria-label="Titanium ring, silver and blue" style="background:linear-gradient(#1f5fbf,#d9d9d9)"></div>
  <div class="name">Vanta – Men's Titanium Ring – Silver and Blue Guy's Band 6mm</div>
  <div class="price">£39.00</div>
</div>
<div class="card" style="left:366px">
  <div class="icons"><svg width="14" height="13" viewBox="0 0 14 13" fill="#c88a10"><path d="M0 1h3l2 8h7l2-6H4" fill="none" stroke="#c88a10" stroke-width="1.6"/><circle cx="6" cy="11.5" r="1.3"/><circle cx="11" cy="11.5" r="1.3"/></svg><svg width="14" height="13" viewBox="0 0 14 13"><path d="M7 12L1.5 6.5a3 3 0 015-4L7 3l.5-.5a3 3 0 015 4z" fill="none" stroke="#c88a10" stroke-width="1.3"/></svg></div>
  <div class="pic" role="img" aria-label="Tungsten ring with wood and abalone shell inlay" style="background:linear-gradient(#e6e6e6,#6b3b2a)"></div>
  <div class="name">Ridgeline – Men's Tungsten Ring – Wood &amp; Abalone Shell 8mm</div>
  <div class="price">£65.00</div>
</div>
<div class="card active" style="left:621px">
  <div class="icons"><svg width="14" height="13" viewBox="0 0 14 13" fill="#c88a10"><path d="M0 1h3l2 8h7l2-6H4" fill="none" stroke="#c88a10" stroke-width="1.6"/><circle cx="6" cy="11.5" r="1.3"/><circle cx="11" cy="11.5" r="1.3"/></svg><svg width="14" height="13" viewBox="0 0 14 13"><path d="M7 12L1.5 6.5a3 3 0 015-4L7 3l.5-.5a3 3 0 015 4z" fill="none" stroke="#c88a10" stroke-width="1.3"/></svg></div>
  <div class="pic" role="img" aria-label="Black and purple tungsten band" style="background:linear-gradient(#7a2aa8,#151515)"></div>
  <div class="name">Onyra – Men's Tungsten Band – Black and Purple Male Ring 8mm</div>
  <div class="price">£42.00</div>
</div>
<div class="card" style="left:874px">
  <div class="icons"><svg width="14" height="13" viewBox="0 0 14 13" fill="#c88a10"><path d="M0 1h3l2 8h7l2-6H4" fill="none" stroke="#c88a10" stroke-width="1.6"/><circle cx="6" cy="11.5" r="1.3"/><circle cx="11" cy="11.5" r="1.3"/></svg><svg width="14" height="13" viewBox="0 0 14 13"><path d="M7 12L1.5 6.5a3 3 0 015-4L7 3l.5-.5a3 3 0 015 4z" fill="none" stroke="#c88a10" stroke-width="1.3"/></svg></div>
  <div class="pic" role="img" aria-label="Gold and silver titanium ring" style="background:linear-gradient(#e3e3e3,#d4b060)"></div>
  <div class="name">Crestor – Men's Titanium Ring – Gold and Silver 8mm</div>
  <div class="price">£42.00</div>
</div>
<div class="pager"><span></span><span></span><span></span><span></span><span></span></div>

<!-- RING STYLES -->
<section class="styles"></section>
<h2 class="script-title" style="top:1503px;line-height:51px">Seeking Uniqueness? Explore Our Range of Distinct<br>Ring Styles</h2>
<div class="abs" role="img" aria-label="Wood inlay rings on green fern leaves" style="left:224px;top:1634px;width:247px;height:136px;border-radius:6px;background:linear-gradient(135deg,#2f7a2a,#6b4a30 50%,#2f6a25)"></div>
<div class="abs" role="img" aria-label="Meteorite rings against a dark space backdrop" style="left:112px;top:1782px;width:251px;height:153px;border-radius:6px;background:linear-gradient(160deg,#0b0f18,#3a3f4a 55%,#1c4a7a)"></div>
<div class="abs" role="img" aria-label="Abalone shell inlay rings on iridescent shell" style="left:378px;top:1782px;width:202px;height:127px;border-radius:6px;background:linear-gradient(135deg,#3aa39a,#6b8fb8 50%,#9aa85a)"></div>

<div class="style-item" style="top:1654px"><h3>Wood</h3>For the man who loves the outdoors. <em>Wood rings</em> in tungsten and titanium<br>Adventurous | Free Spirited | Down-to-Earth</div>
<div class="style-item" style="top:1749px"><h3>Meteorite</h3><em>Meteorite rings</em> that are out of this world For a completely different style.<br>Unique | Distinctive | Magnificent</div>
<div class="style-item" style="top:1844px"><h3>Abalone Shell</h3>For the ocean loving man <em>Shell rings</em> in tungsten and titanium Iridescent<br>| Vibrant | Stunning</div>

<!-- PERSONALISE -->
<section class="personal"></section>
<h2 class="script-title" style="top:2086px">Personalise and Engrave your Ring</h2>
<div class="personal-copy">
  <p>Add heartfelt meaning and sentiment to your ring with a <em>personalised ring engraving</em>. The perfect way to add that little extra something to your ring, whether for yourself, or as a gift.</p>
  <p>Choose your very own ring engraving to give your ring personal meaning, symbolise your commitment and love, or mark a special date.&nbsp; Whatever you choose to engrave on your ring, your engraving will tell your own personal story and will enrich your ring as a cherished keepsake for years to come.</p>
  <p>Add a name, date, initials, or short message and we will engrave it to the inside of your ring. You will not only have an extraordinary ring but one that is symbolic, meaningful, and full of sentiment.</p>
  <p>Whether you are buying the ring as a gift, as a wedding ring or for yourself, engrave your ring to give it the significance it deserves. You may want your own name, the initials of you and your partner, your wedding date or a short message. Your ring, your engraving, your story.</p>
</div>
<a class="btn-dark" href="#">Personalise Your Ring</a>
<div class="abs" role="img" aria-label="Burgundy velvet ring box holding a silver and gold engraved band" style="left:700px;top:2170px;width:380px;height:420px;background:radial-gradient(ellipse at 50% 62%,#d8d8d8 0%,#7a1820 28%,#4a0a10 52%,rgba(255,255,255,0) 72%)"></div>

<!-- REVIEWS -->
<h2 class="script-title" style="top:2706px">We Love Happy Customers</h2>
<div class="review" style="left:13px;top:2808px;height:188px"><h4>Hannah Brookes</h4><div class="stars">★★★★★</div>My partner wanted a black ring and he is absolutely in love with it. We also purchased the option to have it engraved and the support ......</div>
<div class="review" style="left:392px;top:2787px;height:230px;padding-top:24px"><h4>Marcus Hale</h4><div class="stars">★★★★★</div>I absolutely love my ring, it's so shiny and love the colour of the blue with carbon and will be definitely be buying again from this company again. Speedy delivery and very good customer service.</div>
<div class="review" style="left:771px;top:2808px;height:188px"><h4>Owen Prescott</h4><div class="stars">★★★★★</div>Fantastic service from start to finish, loved the fact I could try the rings before I buy. Communications were excellent, quick replies and always helpful.....</div>
<div class="review" style="left:1149px;top:2808px;height:188px"><h4>Nina</h4><div class="stars">★★★★★</div>This Band has collection</div>

<!-- WEDDING BANNER -->
<section class="wedding">
  <div class="deco-rings" role="img" aria-label="Scattered gold and silver wedding bands"></div>
  <div class="wedding-photo" role="img" aria-label="Two gold wedding bands in a dark leather ring box"></div>
</section>
<h2 class="wedding-title">Men's Wedding Bands</h2>
<div class="wedding-sub">FALL WEDDING SALE- 20% OFF SITEWIDE</div>
<a class="btn-gold" href="#" style="left:264px;top:3288px;width:244px;height:43px">Discover Our Collections</a>

<!-- TRUST -->
<div class="trust-base"></div>
<div class="trust">
  <div class="perk" style="left:84px;top:42px"><svg width="56" height="56" viewBox="0 0 56 56"><circle cx="28" cy="28" r="28" fill="#a4161c"/><circle cx="28" cy="28" r="21" fill="none" stroke="#fff" stroke-width="1.5"/><path d="M15 24h16v10H15zM31 27h6l4 4v3H31z" fill="#fff"/><circle cx="20" cy="36" r="3" fill="#fff"/><circle cx="36" cy="36" r="3" fill="#fff"/></svg>Free Delivery</div>
  <div class="perk" style="left:336px;top:42px"><svg width="56" height="56" viewBox="0 0 56 56"><circle cx="28" cy="28" r="28" fill="#a4161c"/><circle cx="28" cy="28" r="21" fill="none" stroke="#fff" stroke-width="1.5"/><path d="M18 22l10-5 10 5v12l-10 5-10-5z" fill="none" stroke="#fff" stroke-width="2.5"/><path d="M18 22l10 5 10-5M28 27v12" fill="none" stroke="#fff" stroke-width="2"/></svg>Free Returns</div>
  <div class="perk" style="left:585px;top:42px"><svg width="56" height="56" viewBox="0 0 56 56"><circle cx="28" cy="28" r="28" fill="#a4161c"/><circle cx="28" cy="28" r="21" fill="none" stroke="#fff" stroke-width="1.5"/><ellipse cx="24" cy="30" rx="8" ry="6" fill="none" stroke="#fff" stroke-width="2.5"/><ellipse cx="32" cy="26" rx="8" ry="6" fill="none" stroke="#fff" stroke-width="2.5"/></svg>Every Ring Stock</div>
  <div class="perk" style="left:206px;top:123px"><svg width="56" height="56" viewBox="0 0 56 56"><circle cx="28" cy="28" r="28" fill="#a4161c"/><circle cx="28" cy="28" r="21" fill="none" stroke="#fff" stroke-width="1.5"/><circle cx="28" cy="30" r="10" fill="none" stroke="#fff" stroke-width="2.5"/><path d="M28 30v-6M25 17h6" stroke="#fff" stroke-width="2.5"/></svg>Fast Delivery</div>
  <div class="perk" style="left:456px;top:123px"><svg width="56" height="56" viewBox="0 0 56 56"><circle cx="28" cy="28" r="28" fill="#a4161c"/><circle cx="28" cy="28" r="21" fill="none" stroke="#fff" stroke-width="1.5"/><circle cx="28" cy="25" r="5" fill="#fff"/><path d="M19 38a9 8 0 0118 0z" fill="#fff"/><circle cx="16" cy="28" r="2" fill="#fff"/><circle cx="40" cy="28" r="2" fill="#fff"/><circle cx="28" cy="14" r="2" fill="#fff"/></svg>Customer Images</div>
</div>

<!-- FOOTER -->
<div class="brand foot-brand" style="left:112px;top:3706px"><span class="brand-dot" style="width:38px;height:38px"></span>TORVIK LOOPS</div>
<div class="foot-col" style="left:330px"><h5>Quick Links</h5><ul><li>FREE ring sizer</li><li>FREE Delivery |</li><li>Returns and Exchanges</li><li>Try at Home</li><li>Ring Engraving</li></ul></div>
<div class="foot-col" style="left:558px;width:310px"><h5>Ring Guide</h5><ul><li>The Best Tungsten and Titanium Rings - Full Guide</li><li>How is Tungsten or Titanium Ring Size Measured?</li><li>Black, Silver Gold - The best colors for mens tungsten and titanium rings</li><li>Whats better tungsten or titanium for a mens ring</li></ul></div>
<div class="foot-col" style="left:936px"><h5>Important Links</h5><ul><li>Contact Us</li><li>Terms of Service</li><li>Privacy Policy</li><li>Blog</li></ul></div>

<div class="rule" style="top:3971px"></div>
<div class="contact" style="left:112px"><svg width="22" height="26" viewBox="0 0 22 26"><path d="M11 1a9 9 0 019 9c0 7-9 15-9 15S2 17 2 10a9 9 0 019-9z" fill="#fff"/><circle cx="11" cy="10" r="3.5" fill="#7a0e12"/></svg>27 Kestrel Row, Alderbury, AL4 9QT</div>
<div class="contact" style="left:563px"><svg width="24" height="24" viewBox="0 0 24 24"><path d="M5 2l4 1 1.5 5-2.5 2a12 12 0 006 6l2-2.5 5 1.5 1 4-3 3C10 22 2 14 2 5z" fill="#fff"/></svg>01632 960418</div>
<div class="contact" style="left:838px"><svg width="26" height="20" viewBox="0 0 26 20"><rect x="1" y="1" width="24" height="18" fill="#fff"/><path d="M1 1l12 10L25 1M1 19l9-9M25 19l-9-9" fill="none" stroke="#7a0e12" stroke-width="1.5"/></svg>hello@torvikloops.com</div>
<div class="rule" style="top:4045px"></div>

<div class="copy">Copyright © 2024 Torvik Loops All Rights Reserved</div>
<div class="pay"><span></span><span></span><span></span><span></span><span></span><span></span><span></span></div>

</body>
</html>
```